Anzeigengestaltung für Workshops
Zielgruppe
Die KTW-Academy realisiert Workshops für Medienschaffende. Im konkreten Fall soll ein 1-tägiger Workshop für Sprecher*innen in Radio, Podcast und Voice-Over beworben werden.
Aufgabenstellung
Die Anzeige soll in den verschiedenen Social-Media-Kanälen ausgespielt werden. Sie soll cool sein, eher minimalistisch, keinesfalls verspielt oder knallig.
Textbausteine sind:
Die Kunst des ruhigen Atems bei Tag [das ist der Titel der Veranstaltung]
Wie Du gut rüberkommst als Sprecher*in in Radio, Podcast und Voice-Over [das ist die Unterzeile]
Präsenz-Training | KTW-Funkhaus | 15.9.2023 [das sind die Rahmendaten]
ggfs. mit Störer 'jetzt buchen' o.ä.
Logo und Bild der Trainerin sind verpflichtend

```html
<!DOCTYPE html>
<html lang="de">
<head>
<meta charset="utf-8">
<title>Die Kunst des ruhigen Atems bei Tag – KTW-Academy</title>
<link rel="stylesheet" href="https://fonts.googleapis.com/css2?family=Space+Grotesk:wght@500;600&display=swap">
<style>
  :root {
    --blue-deep: #0057e9;
    --blue-stroke: #1a6cff;
    --white: #ffffff;
    --photo-sky: #dfeef4;
    --photo-skin: #d9a08e;
    --photo-green: #8c8a6c;
    --photo-dark: #2a2624;
  }
  * { margin: 0; padding: 0; box-sizing: border-box; }
  html, body { width: 851px; height: 1200px; overflow: hidden; background: var(--blue-deep); }
  .ad {
    position: relative;
    width: 851px;
    height: 1200px;
    background: var(--blue-deep);
    font-family: "Space Grotesk", Arial, sans-serif;
    color: var(--white);
    overflow: hidden;
  }
  .ad__strokes { position: absolute; left: 0; top: 0; }
  .ad__title {
    position: absolute;
    top: 82px;
    left: 0;
    width: 851px;
    text-align: center;
    font-weight: 600;
    font-size: 50px;
    line-height: 55px;
    letter-spacing: -0.5px;
  }
  .ad__rule {
    position: absolute;
    top: 220px;
    left: 553px;
    width: 255px;
    height: 2px;
    background: var(--white);
  }
  .ad__portrait {
    position: absolute;
    top: 279px;
    left: 180px;
    width: 490px;
    height: 566px;
    border-radius: 40px;
    background: linear-gradient(180deg, var(--photo-sky) 0%, var(--photo-skin) 40%, var(--photo-green) 75%, var(--photo-dark) 100%);
  }
  .ad__subtitle {
    position: absolute;
    top: 862px;
    left: 0;
    width: 851px;
    text-align: center;
    font-weight: 500;
    font-size: 29px;
    line-height: 34px;
  }
  .ad__facts {
    position: absolute;
    top: 1018px;
    left: 145px;
    font-weight: 500;
    font-size: 27px;
    letter-spacing: -0.2px;
    white-space: nowrap;
  }
  .ad__brand {
    position: absolute;
    top: 1100px;
    left: 150px;
    display: flex;
    align-items: center;
    gap: 12px;
    font-weight: 600;
    font-size: 34px;
    color: var(--white);
  }
  .ad__brand-mark {
    width: 20px;
    height: 20px;
    border-radius: 50%;
    background: var(--white);
  }
</style>
</head>
<body>
<main class="ad">
  <svg class="ad__strokes" width="851" height="1200" aria-hidden="true">
    <polygon points="0,520 700,60 851,0 851,90 600,300 0,700" fill="var(--blue-stroke)" opacity="0.75"/>
    <polygon points="0,380 520,70 560,90 0,470" fill="var(--blue-stroke)" opacity="0.5"/>
    <polygon points="40,700 851,780 851,1150 600,1040 60,940" fill="var(--blue-stroke)"/>
    <polygon points="0,730 200,760 0,800" fill="var(--blue-stroke)" opacity="0.7"/>
  </svg>

  <h1 class="ad__title">Die Kunst des ruhigen<br>Atems bei Tag</h1>
  <div class="ad__rule" aria-hidden="true"></div>

  <div class="ad__portrait" role="img" aria-label="Porträtfoto der Trainerin"></div>

  <p class="ad__subtitle">Wie Du gut rüberkommst als<br>Sprecher*in in Radio, Podcast und<br>Voice-Over</p>

  <p class="ad__facts">Präsenz-Training | KTW-Funkhaus | 15.9.2023</p>

  <div class="ad__brand">
    <span class="ad__brand-mark"></span>
    <span class="ad__brand-name">KTW-Academy</span>
  </div>
</main>
</body>
</html>
```